Freelance Translator in Need of a Business Card

I am a freelance Japanese to English translator. I work in the video game localization industry and do literary translation in my spare time. I would like to have both the English word 'Translator' and the Japanese '翻訳者' in the job title. The final design should evoke trust, openness, and reliability.

Target Market(s)

Video game localization companies
Japanese comic book artists

Industry/Entity Type

Business

Contact Information for Business Card

Daniel Oskerby, Translator
dan.oskerby@fernlowmail.com
velmotranslates.com
twitter: @velmo_tl

Colors

Designer to choose colors to be used in the design.

```html
<!DOCTYPE html>
<html lang="en">
<head>
<meta charset="utf-8">
<title>Velmo Translates — Business Card</title>
<link rel="stylesheet" href="https://fonts.googleapis.com/css2?family=Playfair+Display:wght@700&family=Libre+Baskerville&family=Noto+Serif+JP:wght@400&display=swap">
<style>
  :root {
    --backdrop: #e9e6e1;
    --card-white: #ffffff;
    --card-black: #2b2b2b;
    --ink: #1a1a1a;
    --ink-soft: #4a4a4a;
    --rule: #1f1f1f;
    --divider: #bdbdbd;
    --paper-text: #f2f2f2;
  }
  * { margin: 0; padding: 0; box-sizing: border-box; }
  html, body {
    width: 1200px;
    height: 892px;
    overflow: hidden;
  }
  body {
    background: var(--backdrop);
    display: flex;
    align-items: center;
    justify-content: center;
    gap: 64px;
    font-family: "Libre Baskerville", Georgia, serif;
  }
  .card {
    position: relative;
    width: 504px;
    height: 288px;
    border-radius: 3px;
    box-shadow: 0 10px 28px rgba(0,0,0,0.18), 0 2px 4px rgba(0,0,0,0.12);
    overflow: hidden;
  }

  /* Front */
  .card-front { background: var(--card-white); color: var(--ink); }
  .card-front .brand {
    position: absolute;
    left: 44px;
    top: 48px;
    font-family: "Playfair Display", Georgia, serif;
    font-weight: 700;
    font-size: 29px;
    letter-spacing: 0.3px;
  }
  .rule {
    position: absolute;
    height: 3px;
    background: var(--rule);
  }
  .rule-top { left: 44px; width: 350px; top: 104px; }
  .rule-bottom { left: 196px; width: 264px; top: 236px; }
  .holder {
    position: absolute;
    left: 104px;
    top: 138px;
  }
  .holder-name {
    font-size: 15px;
    color: var(--ink-soft);
    letter-spacing: 0.2px;
  }
  .holder-role {
    margin-top: 4px;
    font-size: 10px;
    color: var(--ink-soft);
  }
  .holder-role .jp {
    font-family: "Noto Serif JP", serif;
    font-size: 11px;
    color: var(--ink);
  }
  .contact {
    position: absolute;
    left: 288px;
    top: 122px;
    padding-left: 16px;
    border-left: 1px solid var(--divider);
    font-size: 10.5px;
    line-height: 1.55;
    color: var(--ink-soft);
  }

  /* Back */
  .card-back {
    background: radial-gradient(ellipse at 40% 40%, #353535 0%, var(--card-black) 70%);
    color: var(--paper-text);
    display: flex;
    flex-direction: column;
    justify-content: center;
    padding-left: 92px;
  }
  .card-back .brand {
    font-family: "Playfair Display", Georgia, serif;
    font-weight: 700;
    font-size: 38px;
    letter-spacing: 0.5px;
  }
  .card-back .url {
    margin-top: 6px;
    font-size: 15px;
    letter-spacing: 0.3px;
    color: #d9d9d9;
  }
</style>
</head>
<body>
  <section class="card card-front" aria-label="Card front">
    <h1 class="brand">Velmo Translates</h1>
    <div class="rule rule-top"></div>
    <div class="holder">
      <p class="holder-name">Daniel Oskerby</p>
      <p class="holder-role">Translator <span class="jp" lang="ja">翻訳者</span></p>
    </div>
    <address class="contact" style="font-style:normal">
      www.velmotranslates.com<br>
      dan.oskerby@fernlowmail.com<br>
      twitter: @velmo_tl
    </address>
    <div class="rule rule-bottom"></div>
  </section>

  <section class="card card-back" aria-label="Card back">
    <h2 class="brand">Velmo Translates</h2>
    <p class="url">www.velmotranslates.com</p>
  </section>
</body>
</html>
```